Complete the design for a website wireframe

I need someone to follow the attached wireframe and update the design including icons, pictures and graphics to compliment the copy. I want to have good transitions between sections. All items need to be included as separate files.

Target Market(s)

IT Executives

Number of Pages Required

3 page

Colors
0054AA
0677BA
7BADD7
CADEEF
E8F1F8
F0912C
F2A743
F7CA91
FBE8D2
FDF5EE

```html
<!DOCTYPE html>
<html lang="en">
<head>
<meta charset="utf-8">
<title>NovaSky Solutions – Technology Advisory</title>
<link rel="stylesheet" href="https://fonts.googleapis.com/css2?family=Lexend:wght@400;500;600;700&family=Nunito+Sans:wght@400;600;700;800&display=swap">
<style>
:root{
  --blue-900:#0b2a7a;
  --blue-800:#0e3a96;
  --blue:#0054AA;
  --blue-mid:#0677BA;
  --blue-soft:#7BADD7;
  --blue-pale:#CADEEF;
  --blue-mist:#E8F1F8;
  --orange:#e0691e;
  --orange-2:#F0912C;
  --orange-3:#F2A743;
  --peach:#F7CA91;
  --cream:#FBE8D2;
  --cream-2:#FDF5EE;
  --ink:#1b1b1f;
  --text:#55575d;
  --footer:#0e1424;
  --white:#fff;
}
*{box-sizing:border-box;margin:0;padding:0}
html,body{width:1200px;height:5268px;overflow:hidden}
body{font-family:"Nunito Sans",Arial,sans-serif;color:var(--text);background:var(--white);position:relative}
h1,h2,h3,h4,.btn,.brand{font-family:"Lexend",Arial,sans-serif}
.abs{position:absolute}
.btn{display:inline-flex;align-items:center;justify-content:center;height:48px;padding:0 36px;border-radius:24px;background:var(--orange);color:#fff;font-size:13px;font-weight:600;letter-spacing:.4px;text-transform:uppercase;text-decoration:none}
.btn--ghost{background:#fff;color:var(--ink);border:2px solid var(--orange)}
.photo{display:block}

/* nav */
.site-nav{top:0;left:0;width:1200px;height:102px;border-top:4px solid var(--blue);background:#fff}
.brand{display:flex;align-items:center;gap:12px;font-size:30px;font-weight:600;color:var(--blue);text-decoration:none}
.brand-dot{width:44px;height:44px;border-radius:50%;border:5px solid var(--orange)}
.site-nav .brand{position:absolute;left:110px;top:22px}
.nav-links{position:absolute;left:572px;top:40px;display:flex;gap:46px;list-style:none;font-family:"Lexend",sans-serif;font-size:15px;font-weight:500;color:var(--ink)}
.site-nav .btn{position:absolute;left:900px;top:26px;height:50px;padding:0 28px}

/* hero */
.hero{top:102px;left:0;width:1200px;height:600px;background:linear-gradient(110deg,#0a1a4e 0%,#13307a 45%,#1e4a94 75%,#3b6aa8 100%)}
.hero-copy{position:absolute;left:0;top:210px;width:1200px;text-align:center;color:#fff}
.hero-copy h1{font-size:29px;font-weight:600}
.hero-copy p{font-size:16px;font-weight:700;line-height:26px;margin:18px auto 20px;width:460px}
.hero-copy .btn{height:46px;padding:0 24px}
.feature-bar{top:664px;left:110px;width:978px;height:74px;border-radius:30px;background:var(--blue-900);display:flex;justify-content:space-around;align-items:center;color:#fff;font-size:16px;font-weight:600}
.feature-bar span{display:flex;align-items:center;gap:12px}

/* overwhelming */
.section-title{font-size:29px;font-weight:600;color:var(--ink);text-align:center}
.eyebrow{font-family:"Lexend",sans-serif;font-size:17px;color:var(--blue);text-align:center}
.rule{width:210px;height:2px;background:var(--blue-soft);margin:12px auto 0}
.intro{top:830px;left:0;width:1200px;text-align:center}
.intro p{width:830px;margin:36px auto 0;font-size:14px;line-height:26px}
.value-cards{top:1000px;left:110px;width:978px;display:flex;gap:16px}
.value-card{flex:1;height:242px;background:#fff;box-shadow:0 3px 14px rgba(0,0,0,.12);border-radius:3px;text-align:center;padding-top:34px}
.icon-circle{width:96px;height:96px;border-radius:50%;background:var(--orange);margin:0 auto;display:flex;align-items:center;justify-content:center;box-shadow:0 0 0 3px #fff,0 0 0 5px var(--orange)}
.value-card h3{font-family:"Nunito Sans",sans-serif;font-size:16px;font-weight:800;color:var(--ink);line-height:26px;margin-top:28px;padding:0 20px}

/* split expert */
.expert{top:1340px;left:0;width:1200px;height:580px;display:flex}
.expert .photo{width:600px;height:580px;background:linear-gradient(135deg,#0d1e4a,#1b4f96 55%,#5d90c8)}
.expert-copy{width:600px;background:var(--blue-pale);padding:44px 110px 0 42px}
.expert-copy .eyebrow{text-align:left}
.expert-copy h2{font-size:29px;font-weight:600;color:var(--ink);margin:8px 0 20px}
.expert-copy p{font-size:13.5px;line-height:25.5px;text-align:justify;margin-bottom:14px}
.expert-copy p.strong{font-weight:800;color:var(--ink)}
.ticks{list-style:none;margin-bottom:30px}
.ticks li{display:flex;align-items:center;gap:14px;font-size:13.5px;line-height:32px}
.expert-copy .btn{height:46px;padding:0 26px}

/* stages */
.stages-head{top:2010px;left:0;width:1200px;text-align:center}
.stages-head h2{font-size:29px;font-weight:600;color:var(--ink);margin-top:6px}
.stage-cards{top:2124px;left:110px;width:978px;display:flex;gap:10px}
.stage-card{flex:1;height:392px;background:#fff;box-shadow:0 3px 14px rgba(0,0,0,.12);text-align:center}
.stage-card .photo{height:206px}
.stage-card h3{font-size:15px;font-weight:600;color:var(--blue);margin:26px 0 12px}
.stage-card p{font-size:13px;line-height:22px;padding:0 18px}
.stage-card a{display:block;margin-top:14px;font-size:11px;color:var(--orange);text-decoration:underline}

/* partners */
.partners{top:2616px;left:0;width:1200px;height:284px;background:var(--orange)}
.partners h2{text-align:center;color:#fff;font-size:29px;font-weight:500;margin-top:58px}
.partner-row{position:absolute;left:110px;top:132px;display:flex;gap:22px}
.partner-badge{width:178px;height:88px;background:#fff;border-radius:5px;display:flex;align-items:center;justify-content:center}
.partner-badge i{display:block;width:110px;height:26px;border-radius:13px;background:var(--blue-pale)}
.arrow{position:absolute;top:158px;width:36px;height:36px}

/* steps */
.steps-head{top:2990px;left:0;width:1200px;text-align:center}
.steps-head h2{font-size:29px;font-weight:600;color:var(--ink);margin-top:8px}
.steps{top:3108px;left:110px;width:978px;display:flex}
.step{flex:1;text-align:center}
.step-icon{width:104px;height:104px;border-radius:50%;background:#fff;box-shadow:0 3px 14px rgba(0,0,0,.14);margin:0 auto;display:flex;align-items:center;justify-content:center}
.step h3{font-size:16px;font-weight:600;color:var(--blue);margin:38px 0 12px;letter-spacing:.3px}
.step p{font-size:13.5px;line-height:24px;width:290px;margin:0 auto}
.step-actions{top:3400px;left:0;width:1200px;display:flex;justify-content:center;gap:10px}
.step-actions .btn{height:48px;padding:0 36px}

/* advisor */
.advisor{top:3548px;left:0;width:1200px;height:524px;display:flex}
.advisor-copy{width:600px;background:var(--cream);padding:52px 30px 0 110px}
.advisor-copy h2{font-size:25px;font-weight:600;color:var(--ink)}
.advisor-copy .lead{font-size:13.5px;font-weight:700;color:var(--blue);line-height:25px;margin:14px 0 18px}
.advisor-copy p{font-size:13.5px;line-height:26px;margin-bottom:16px}
.advisor-copy .btn{height:46px;padding:0 26px;margin-top:18px}
.advisor .photo{width:600px;height:524px;background:linear-gradient(140deg,#0a2a3c,#15607a 55%,#2aa0b8)}

/* growth band */
.growth{top:4072px;left:0;width:1200px;height:258px;background:linear-gradient(100deg,var(--blue-800),var(--blue));color:#fff;text-align:center}
.growth h2{font-size:29px;font-weight:500;margin-top:82px}
.growth p{font-family:"Lexend",sans-serif;font-size:17px;line-height:30px;width:980px;margin:18px auto 0}

/* spotlight */
.spot-frame{top:4436px;left:110px;width:410px;height:384px;background:#fff;box-shadow:0 3px 14px rgba(0,0,0,.18);padding:10px}
.spot-frame .photo{width:100%;height:100%;background:linear-gradient(140deg,#0a0f22,#1c2b55 60%,#3e5f9a)}
.spot-small{top:4650px;left:370px;width:200px;height:224px;background:#fff;box-shadow:0 3px 14px rgba(0,0,0,.22);padding:10px}
.spot-small .photo{width:100%;height:100%;background:linear-gradient(160deg,#1a2230,#394a62)}
.spot-copy{top:4462px;left:640px;width:450px}
.spot-copy h2{font-size:23px;font-weight:600;color:var(--ink);margin-bottom:30px}
.spot-copy p{font-size:13.5px;line-height:26px;margin-bottom:18px}
.spot-copy .btn{height:46px;padding:0 26px;margin-top:10px}

/* footer */
.site-footer{top:4945px;left:0;width:1200px;height:275px;background:var(--footer);color:#fff}
.site-footer .brand{position:absolute;left:110px;top:52px;color:#fff}
.site-footer .blurb{position:absolute;left:110px;top:150px;width:340px;font-size:13px;font-weight:700;line-height:23px}
.foot-col{position:absolute;top:48px}
.foot-col h4{font-size:16px;font-weight:600;margin-bottom:20px}
.foot-col ul{list-style:none;font-size:13px}
.foot-col li{display:flex;align-items:center;gap:14px;line-height:25px}
.foot-col li::before{content:"";width:12px;height:12px;border-radius:50%;background:var(--orange)}
.site-footer .btn{position:absolute;left:916px;top:48px;height:46px;padding:0 26px}
.socials{position:absolute;left:944px;top:130px;display:flex;gap:12px}
.socials span{width:32px;height:32px;border-radius:50%;border:2px solid #fff;display:block}
.copyright{top:5220px;left:0;width:1200px;height:48px;background:#161208;color:var(--orange-2);font-size:12px;display:flex;align-items:center;justify-content:center}
</style>
</head>
<body>

<header class="site-nav abs">
  <a class="brand" href="#"><span class="brand-dot"></span>NovaSky Solutions</a>
  <ul class="nav-links"><li>Services &#8964;</li><li>Solutions</li><li>About</li></ul>
  <a class="btn" href="#">Schedule a Call</a>
</header>

<section class="hero abs" role="img" aria-label="Photo: two engineers working in a data center server aisle">
  <div class="hero-copy">
    <h1>Get Clarity on Your Technology Roadmap</h1>
    <p>Partner with a Trusted Advisor for Voice, Data, Cloud and Security Solutions</p>
    <a class="btn" href="#">Schedule a Call</a>
  </div>
</section>

<div class="feature-bar abs">
  <span><svg width="16" height="16" viewBox="0 0 16 16"><rect x="1" y="3" width="12" height="12" fill="none" stroke="#fff" stroke-width="1.6"/><path d="M4 8l3 3 8-9" fill="none" stroke="#fff" stroke-width="2"/></svg>Stay Ahead of Disruption</span>
  <span><svg width="16" height="16" viewBox="0 0 16 16"><rect x="1" y="3" width="12" height="12" fill="none" stroke="#fff" stroke-width="1.6"/><path d="M4 8l3 3 8-9" fill="none" stroke="#fff" stroke-width="2"/></svg>Outpace the Competition</span>
  <span><svg width="16" height="16" viewBox="0 0 16 16"><rect x="1" y="3" width="12" height="12" fill="none" stroke="#fff" stroke-width="1.6"/><path d="M4 8l3 3 8-9" fill="none" stroke="#fff" stroke-width="2"/></svg>Lead Future Growth</span>
</div>

<section class="intro abs">
  <h2 class="section-title">Technology Shouldn't Be Overwhelming</h2>
  <div class="rule"></div>
  <p>Many business leaders struggle to keep pace with rapidly changing technology. Thousands of tech companies offer innovative solutions. But finding the RIGHT provider is overwhelming when you aren't certain you will:</p>
</section>

<div class="value-cards abs">
  <div class="value-card"><div class="icon-circle"><svg width="50" height="50" viewBox="0 0 50 50"><circle cx="25" cy="25" r="20" fill="none" stroke="#fff" stroke-width="3"/><text x="25" y="33" text-anchor="middle" font-family="Lexend,sans-serif" font-size="24" fill="#fff">$</text></svg></div><h3>Receive the best price and value</h3></div>
  <div class="value-card"><div class="icon-circle"><svg width="50" height="50" viewBox="0 0 50 50" fill="none" stroke="#fff" stroke-width="2.5"><circle cx="25" cy="20" r="9"/><circle cx="25" cy="20" r="3"/><path d="M8 30c6 4 10 10 17 12 7-2 11-8 17-12"/></svg></div><h3>Successfully integrate the new solution</h3></div>
  <div class="value-card"><div class="icon-circle"><svg width="50" height="50" viewBox="0 0 50 50" fill="none" stroke="#fff" stroke-width="2.5"><path d="M14 30a8 8 0 0 1 2-16 11 11 0 0 1 20 2 7 7 0 0 1 0 14z"/><path d="M18 36l7 5 7-5M25 30v11"/></svg></div><h3>Receive expert ongoing support</h3></div>
  <div class="value-card"><div class="icon-circle"><svg width="50" height="50" viewBox="0 0 50 50" fill="none" stroke="#fff" stroke-width="2.5"><path d="M8 42h36M14 40V30M22 40V24M30 40V28M38 40V18M12 24l10-8 8 6 12-12"/></svg></div><h3>Invest in a solution that remains relevant</h3></div>
</div>

<section class="expert abs">
  <div class="photo" role="img" aria-label="Photo: engineer reviewing data on several monitors"></div>
  <div class="expert-copy">
    <div class="eyebrow">Streamline Your Business With</div>
    <h2>Expert-Vetted Tech Solutions</h2>
    <p>At NovaSky, we understand how frustrating working with technology providers can be. Not only do you face time-consuming meetings and demos... You also risk investing in a solution that won't deliver as promised.</p>
    <p class="strong">Our process takes the headache out of sourcing the RIGHT tech solutions for your business.</p>
    <p>You get a custom plan to implement at every stage, so you can:</p>
    <ul class="ticks">
      <li><svg width="14" height="14" viewBox="0 0 16 16"><rect x="1" y="3" width="12" height="12" fill="none" stroke="#0054AA" stroke-width="1.6"/><path d="M4 8l3 3 8-9" fill="none" stroke="#0054AA" stroke-width="2"/></svg>Protect against security threats</li>
      <li><svg width="14" height="14" viewBox="0 0 16 16"><rect x="1" y="3" width="12" height="12" fill="none" stroke="#0054AA" stroke-width="1.6"/><path d="M4 8l3 3 8-9" fill="none" stroke="#0054AA" stroke-width="2"/></svg>Stay ahead of your competition</li>
      <li><svg width="14" height="14" viewBox="0 0 16 16"><rect x="1" y="3" width="12" height="12" fill="none" stroke="#0054AA" stroke-width="1.6"/><path d="M4 8l3 3 8-9" fill="none" stroke="#0054AA" stroke-width="2"/></svg>Confidently scale your business</li>
    </ul>
    <a class="btn" href="#">More on the Process</a>
  </div>
</section>

<section class="stages-head abs">
  <div class="eyebrow">Custom Solutions and</div>
  <h2>Support At Every Stage</h2>
</section>

<div class="stage-cards abs">
  <article class="stage-card">
    <div class="photo" role="img" aria-label="Photo: two colleagues working at computer screens" style="background:linear-gradient(135deg,#0f2150,#2e5a9a)"></div>
    <h3>DIGITAL TRANSFORMATION</h3>
    <p>Need to upgrade a legacy solution or invest in a new one? We'll help you create a custom plan for a seamless transition.</p>
    <a href="#">Get a Roadmap for Transformation</a>
  </article>
  <article class="stage-card">
    <div class="photo" role="img" aria-label="Photo: hands typing on a laptop with security graphics" style="background:linear-gradient(135deg,#8a8f99,#d6d9de)"></div>
    <h3>SECURE YOUR BUSINESS</h3>
    <p>Leverage our expertise to identify the systems and tools needed to scale your business with confidence.</p>
    <a href="#">Learn How To Protect Your Business</a>
  </article>
  <article class="stage-card">
    <div class="photo" role="img" aria-label="Photo: hand touching a glowing tablet screen" style="background:linear-gradient(135deg,#0b1020,#3a2a30 70%,#7a4a30)"></div>
    <h3>OPTIMIZE EXPENSES</h3>
    <p>Ready to optimize, but unsure where to start? We'll help you pinpoint existing tech obstacles, create a custom</p>
    <a href="#">Get A Detailed Analysis</a>
  </article>
</div>

<section class="partners abs">
  <h2>Our Trusted Partners...</h2>
  <svg class="arrow" style="left:44px" viewBox="0 0 36 36"><path d="M22 6L10 18l12 12" fill="none" stroke="#fff" stroke-width="4"/></svg>
  <div class="partner-row">
    <div class="partner-badge"><i></i></div>
    <div class="partner-badge"><i></i></div>
    <div class="partner-badge"><i></i></div>
    <div class="partner-badge"><i></i></div>
    <div class="partner-badge"><i></i></div>
  </div>
  <svg class="arrow" style="left:1122px" viewBox="0 0 36 36"><path d="M14 6l12 12-12 12" fill="none" stroke="#fff" stroke-width="4"/></svg>
</section>

<section class="steps-head abs">
  <div class="eyebrow">Here's How To</div>
  <h2>Make Tech Decisions With Confidence</h2>
</section>

<div class="steps abs">
  <div class="step">
    <div class="step-icon"><svg width="46" height="46" viewBox="0 0 46 46"><rect x="4" y="8" width="38" height="32" rx="3" fill="none" stroke="#0054AA" stroke-width="2.5"/><rect x="4" y="8" width="38" height="8" fill="#e0691e"/><g fill="#0054AA"><rect x="10" y="21" width="5" height="4"/><rect x="20" y="21" width="5" height="4"/><rect x="30" y="21" width="5" height="4"/><rect x="10" y="30" width="5" height="4"/><rect x="20" y="30" width="5" height="4"/><rect x="30" y="30" width="5" height="4"/></g></svg></div>
    <h3>SCHEDULE A CALL</h3>
    <p>We'll take time to understand your unique needs, then determine your best next steps.</p>
  </div>
  <div class="step">
    <div class="step-icon"><svg width="46" height="46" viewBox="0 0 46 46" fill="none" stroke="#0054AA" stroke-width="2.5"><path d="M12 26a8 8 0 0 1 2-15 10 10 0 0 1 18 2 7 7 0 0 1 0 13z"/><path d="M23 26v12M16 30v6M30 30v6"/><circle cx="23" cy="40" r="2" fill="#e0691e" stroke="none"/></svg></div>
    <h3>DEVELOP A ROADMAP</h3>
    <p>With our outcome-driven approach, you get a clear plan and implementation at every stage.</p>
  </div>
  <div class="step">
    <div class="step-icon"><svg width="46" height="46" viewBox="0 0 46 46" fill="none" stroke="#0054AA" stroke-width="2.5"><path d="M6 40h34M10 38V28M18 38V22M26 38V18M34 38V12"/><circle cx="12" cy="12" r="4" stroke="#e0691e"/></svg></div>
    <h3>LEAD FUTURE GROWTH</h3>
    <p>Confidently grow your business and stay ahead of disruption and the competition.</p>
  </div>
</div>

<div class="step-actions abs">
  <a class="btn" href="#">Schedule a Call</a>
  <a class="btn btn--ghost" href="#">Take Back Your Time</a>
</div>

<section class="advisor abs">
  <div class="advisor-copy">
    <h2>How Will an IT Advisor Help You?</h2>
    <p class="lead">Do you really want to vet and negotiate with each service provider yourself?</p>
    <p>A trusted IT advisor reduces the time and energy it takes to source and implement tech solutions. We'll take the time to know your business and understand your needs. Then, we'll use our objective, in-depth approach to find the BEST solution for your business, at a great price.</p>
    <p>You'll walk away with a custom roadmap to easily implement your new tech solution. Plus, leverage our expert support at any time if you run into snags with your provider.</p>
    <a class="btn" href="#">Meet Dana</a>
  </div>
  <div class="photo" role="img" aria-label="Photo: hands on a laptop with holographic technology graphics"></div>
</section>

<section class="growth abs">
  <h2>Secure Future Business Growth</h2>
  <p>Don't wait another day. There's too much at risk. Get the direction you need to streamline internal processes. Create an exceptional experience for customers AND employees.</p>
</section>

<div class="spot-frame abs"><div class="photo" role="img" aria-label="Illustration: hand touching a cloud network diagram"></div></div>
<div class="spot-small abs"><div class="photo" role="img" aria-label="Photo: technician working in a server room"></div></div>

<section class="spot-copy abs">
  <h2>Spotlight Lead Generator Here</h2>
  <p>Sed ut perspiciatis unde omnis iste natus error sit voluptatem accusantium doloremque laudantium, totam rem aperiam, eaque ipsa quae ab illo inventore veritatis et quasi architecto beatae vitae dicta sunt explicabo.</p>
  <p>At vero eos et accusamus et iusto odio dignissimos ducimus qui blanditiis praesentium voluptatum deleniti atque corrupti quos dolores et quas molestias.</p>
  <a class="btn" href="#">Download Now</a>
</section>

<footer class="site-footer abs">
  <a class="brand" href="#"><span class="brand-dot"></span>NovaSky Solutions</a>
  <p class="blurb">Helping business leaders source and implement custom technology solutions to stay ahead of disruption and outpace their competition.</p>
  <div class="foot-col" style="left:498px"><h4>Quick Links</h4><ul><li>Services</li><li>Solution</li><li>Process</li><li>About</li><li>Contact</li></ul></div>
  <div class="foot-col" style="left:690px"><h4>Other Links</h4><ul><li>Case Study</li><li>Partners</li></ul></div>
  <a class="btn" href="#">Schedule a Call</a>
  <div class="socials"><span></span><span></span><span></span></div>
</footer>
<div class="copyright abs">Copyright 2021 NovaSky © All Rights Reserved.</div>

</body>
</html>
```